We need a flyer for our company. We test drugs, laser, LED or other light sources for phototoxicity on healthy volunteers.
You can use our website for an idea or imagine www.lumivanta.co.uk
Lumivanta has a well-established reputation in the field of drug- and chemical-induced phototoxicity and expertise in clinical studies of photoprotective agents, such as nutraceuticals and antioxidants and light-based device development and application. The team at Lumivanta has an international reputation in the field of UV and visible light measurement and our team has a truly multidisciplinary nature, with professionals including physicians, medical physicists, biochemists, technicians and nurses.

Target Market(s)

any pharmaceutical or cosmetical company

Industry/Entity Type

Cosmetic

Font styles to use
Serif

Colors

Designer to choose colors to be used in the design.

Requirements
Must have
• Clinical studies:
• Phototoxicity
• Photoallergy to topical agents
• Photoprotection by oral or topical agents
• Light-based devices
• Laboratory studies:
• Photosafety and photoxicity
• Photophysics and light source evaluation
Nice to have
• Can you reduce the amount of text and concentrate on this point?
• First page:
• • Lumivanta has a well-established reputation in the field of drug- and chemical-induced phototoxicity and expertise in clinical studies of photoprotective agents:
• such as nutraceuticals
• and antioxidants
• and light-based device development and application.
• • The team at Lumivanta has an international reputation in the field of UV and visible light measurement and our team has a truly multidisciplinary nature, with professionals including physicians, medical physicists, biochemists, technicians and nurses
• Second page:
• Clinical studies
• Phototoxicity
• Light-based devices
• Laboratory studies

```html
<!DOCTYPE html>
<html lang="en">
<head>
<meta charset="utf-8">
<title>Lumivanta Flyer</title>
<link rel="stylesheet" href="https://fonts.googleapis.com/css2?family=Open+Sans:wght@400;600;700&display=swap">
<style>
  :root{
    --stage:#1a6f96;
    --navy:#0f4c7a;
    --blue:#1f86c4;
    --sky:#5fb6e0;
    --pale:#bfe2f3;
    --paper:#ffffff;
    --ink:#1e2a33;
  }
  *{margin:0;padding:0;box-sizing:border-box}
  html,body{width:1200px;height:1000px;overflow:hidden}
  body{background:var(--stage);font-family:"Open Sans",Arial,sans-serif;color:var(--ink);position:relative}
  .page{position:absolute;top:217px;width:400px;height:566px;background:var(--paper);overflow:hidden;box-shadow:0 18px 40px rgba(0,0,0,.28)}
  .page--front{left:150px}
  .page--back{left:650px}
  .page svg.shapes{position:absolute;inset:0}
  .logo{position:absolute;background:var(--navy);border:2px solid var(--paper);outline:1px solid var(--navy);border-radius:3px;color:var(--paper);font-weight:700;font-size:15px;line-height:30px;padding:0 14px}
  .page--front .logo{top:16px;right:16px}
  .page--back .logo{top:18px;right:16px}
  .photo{position:absolute}
  .services{position:absolute;left:44px;top:358px;list-style:none;font-size:12.5px;line-height:17px;color:var(--ink)}
  .services li::before{content:"- "}
  .site{position:absolute;right:22px;bottom:24px;font-size:9px;color:var(--paper)}
  .intro{position:absolute;left:264px;top:200px;width:128px;font-size:8.5px;line-height:11px;color:var(--ink)}
  .team{position:absolute;left:36px;top:414px;width:330px;font-size:11.5px;line-height:15.5px;color:var(--ink)}
  .contact-icons{position:absolute;right:30px;top:334px;display:flex;gap:14px}
  .contact-icons span{width:18px;height:18px;border-radius:50%;background:var(--paper);display:flex;align-items:center;justify-content:center}
</style>
</head>
<body>

<section class="page page--front">
  <svg class="shapes" width="400" height="566" viewBox="0 0 400 566">
    <polygon points="0,80 40,58 400,58 400,80" fill="var(--pale)"/>
    <polygon points="0,92 60,70 80,70 20,92" fill="var(--blue)"/>
    <polygon points="30,92 90,70 110,70 50,92" fill="var(--sky)"/>
    <polygon points="0,160 400,140 400,200 0,200" fill="var(--pale)"/>
    <polygon points="210,330 400,300 400,340 250,340" fill="var(--navy)"/>
    <polygon points="270,330 400,312 400,326 290,336" fill="var(--blue)"/>
    <polygon points="0,548 400,506 400,566 0,566" fill="var(--blue)"/>
    <polygon points="0,548 60,542 48,566 0,566" fill="var(--pale)"/>
  </svg>
  <div class="photo" role="img" aria-label="Laboratory technician working under a blue UV light bench"
       style="left:14px;top:92px;width:265px;height:118px;background:linear-gradient(120deg,#1b2550,#4a5aa8 55%,#c9d4f0);clip-path:polygon(0 0,95% 0,100% 50%,93% 100%,0 100%)"></div>
  <div class="photo" role="img" aria-label="Researcher in a lab coat showing a tablet to a volunteer"
       style="left:40px;top:200px;width:360px;height:140px;background:linear-gradient(90deg,#f1f3f6,#e4e8ee 50%,#d8dde5);clip-path:polygon(0 0,100% 0,100% 62%,60% 100%,0 100%)"></div>
  <div class="logo">Lumivanta</div>
  <ul class="services">
    <li>Clinical studies</li>
    <li>Phototoxicity</li>
    <li>Photoallergy to topical agents</li>
    <li>Photoprotection by oral or topical agents</li>
    <li>Light-based devices</li>
    <li>Laboratory studies</li>
    <li>Photosafety and photoxicity</li>
    <li>Photophysics and light source evaluation</li>
  </ul>
  <div class="site">www.lumivanta.co.uk</div>
</section>

<section class="page page--back">
  <svg class="shapes" width="400" height="566" viewBox="0 0 400 566">
    <polygon points="230,0 400,0 400,140" fill="var(--blue)"/>
    <polygon points="0,215 250,215 250,228 0,228" fill="var(--navy)"/>
    <polygon points="245,218 262,218 252,262 262,318 245,318 235,262" fill="var(--sky)"/>
    <polygon points="0,392 245,392 260,405 0,405" fill="var(--navy)"/>
    <polygon points="248,325 400,325 400,362 262,362" fill="var(--blue)"/>
    <polygon points="0,392 230,392 215,404 0,404" fill="var(--blue)"/>
  </svg>
  <div class="photo" role="img" aria-label="Clinical team standing in front of a library bookcase"
       style="left:0;top:52px;width:250px;height:163px;background:linear-gradient(180deg,#7a5a3e,#a8876a 60%,#cdb9a5)"></div>
  <div class="photo" role="img" aria-label="Nurse setting up a light device beside a volunteer"
       style="left:262px;top:62px;width:114px;height:126px;background:linear-gradient(160deg,#9a6f4d,#c8a482 55%,#6f8f99);border:3px solid var(--pale)"></div>
  <div class="photo" role="img" aria-label="Clinical test room with a phototesting chair and lamp"
       style="left:0;top:228px;width:245px;height:164px;background:linear-gradient(180deg,#eef1f3,#d7dde1 60%,#9aa3aa)"></div>
  <div class="logo">Lumivanta</div>
  <p class="intro">Lumivanta has a well-established reputation in the field of drug- and chemical-induced phototoxicity and expertise in clinical studies of photoprotective agents: - such as nutraceuticals - and antioxidants - and light-based device development and application.</p>
  <div class="contact-icons">
    <span aria-label="Location"><svg width="10" height="10" viewBox="0 0 10 10"><path d="M5 1a3 3 0 0 1 3 3c0 2-3 5-3 5S2 6 2 4a3 3 0 0 1 3-3z" fill="var(--blue)"/></svg></span>
    <span aria-label="Phone"><svg width="10" height="10" viewBox="0 0 10 10"><path d="M2 1l2 2-1 1.2a6 6 0 0 0 2.8 2.8L7 6l2 2-1.2 1.2C4.5 9 1 5.5.8 2.2z" fill="var(--blue)"/></svg></span>
    <span aria-label="Email"><svg width="10" height="10" viewBox="0 0 10 10"><rect x="1" y="2.5" width="8" height="5.5" fill="var(--blue)"/><path d="M1 2.5l4 3 4-3" stroke="#fff" stroke-width=".8" fill="none"/></svg></span>
  </div>
  <p class="team">The team of Lumivanta has an international reputation in the field of UV and visible light measurement and our team has a truly multidisciplinary nature, with professionals including physicians, medical physicists, biochemists, technicians and nurses.</p>
</section>

</body>
</html>
```